Copper Brook Agency Website - Wordpress Web UPDATED BRIEF

FINAL LOGO UPLOADED - please look to this as reference for how we would like the site to look and feel.

We are a digital marketing agency - looking to have a new website built. We are looking for a simple one page feel of site that will allow us to grow it later. (Feel free to take some liberties with that if your imagination veers off) Must be very, playful, bold, sleek and easily integrate video. Wordpress only.

Overview:

Copper Brook is a creative constellation. We are built on what's great about the shared economy. With access to thousands of content creators, designers, technicians, writers, strategists and other creatives around the world, we are built differently than a traditional “brick and mortar” Marketing Agency. We provide the traditional services our clients have come to expect, without the “5X factor” of covering the overhead common in the old agency model. We believe even better work can be created in collaboration with our clients and by passing those savings back to them for their use. Our clients pay for our art, our work and our passion –not our furniture.

"Copper Brook, Let's Begin Today"

Target Market(s)

companies looking for creative agency help, video production, creative consulting and coaching

Industry/Entity Type

Digital Marketing

Coding

Coded - Design and coding required

Number of Pages Required

1 page

Font styles to use
Sans Serif

Colors
3277b5
33a6d7
ec1f27

Requirements
Must have
• Wordpress design is a must. Looking for a one sheet homepage - with sections that are all on the main front page. We will have videos to embed, and should be able to have client logos and easy access to show a variety of our creative work.
• Please look to the logo for how we would like the site to feel.
• Please think "icon process flow" instead of blocks of text (which we used to have). Use the text to explain what the process flow should represent - don't actually copy paste the text but show it visually in icons.
Nice to have
• innovation around how we show video content. solid colors complementary to our palette and aesthetic.
Should not have
• Standard HTML coding

```html
<!DOCTYPE html>
<html lang="en">
<head>
<meta charset="utf-8">
<title>Copper Brook Agency</title>
<link href="https://fonts.googleapis.com/css2?family=Fjalla+One&family=Open+Sans:wght@400;600;700&display=swap" rel="stylesheet">
<style>
:root{
  --red:#ec1f27;
  --red-dark:#c9161d;
  --sky:#33a6d7;
  --blue:#3277b5;
  --ink:#222;
  --text:#444;
  --light:#f7f7f7;
  --dark:#333;
  --white:#fff;
}
*{margin:0;padding:0;box-sizing:border-box}
html,body{width:1200px;height:3588px;overflow:hidden}
body{position:relative;font-family:"Open Sans",sans-serif;color:var(--text);background:var(--white)}
.head{font-family:"Fjalla One",sans-serif;font-weight:400;text-transform:uppercase}
section{position:absolute;left:0;width:1200px;overflow:hidden}
.abs{position:absolute}

/* hero */
.hero{top:0;height:624px;background:linear-gradient(120deg,#ec1f27 0%,#e8282c 60%,#f05a46 100%)}
.brand{left:100px;top:34px;display:flex;align-items:center;gap:12px}
.brand-dot{width:40px;height:40px;border-radius:50%;background:var(--white)}
.brand-name{font-family:"Fjalla One",sans-serif;font-size:26px;color:var(--white);text-transform:uppercase}
.phone{right:60px;top:18px;display:flex;align-items:center;gap:8px;color:var(--white);font-size:17px}
.hero-title{left:100px;top:222px;font-size:53px;line-height:73px;color:var(--white)}
.hero-title .mark{background:var(--red-dark);color:var(--ink);padding:0 6px}
.hero-art{left:522px;top:278px;width:678px;height:346px;background:linear-gradient(180deg,#f8c9c4 0%,#e9434a 55%,#2a2a2a 100%);border-radius:120px 0 0 0}
.stripes{left:100px;top:470px;width:110px;height:154px;background:repeating-linear-gradient(135deg,rgba(0,0,0,.12) 0 3px,transparent 3px 7px)}
.stripes-top{right:60px;top:0;width:70px;height:150px;background:repeating-linear-gradient(135deg,rgba(0,0,0,.12) 0 3px,transparent 3px 7px)}

/* intro */
.intro{top:624px;height:367px;background:linear-gradient(90deg,#3a3a3a,#4a4643 60%,#5a534d)}
.down{left:575px;top:25px;width:50px;height:50px;border-radius:50%;background:var(--white);display:flex;align-items:center;justify-content:center}
.intro p{position:absolute;left:100px;top:135px;width:1040px;color:var(--white);font-size:18px;line-height:30px}

/* service rows */
.row{height:auto}
.photo{position:absolute;top:0;width:600px;height:100%}
.copy{position:absolute;width:520px}
.copy h2{font-size:31px;color:var(--ink);display:inline-block;padding-bottom:6px;border-bottom:5px solid var(--red)}
.copy h3{margin-top:24px;font-size:18px;line-height:25px;color:var(--blue);font-weight:700;text-transform:uppercase}
.copy p{margin-top:12px;font-size:15px;line-height:25px;color:var(--text)}
.discovery{top:991px;height:346px;background:var(--light)}
.strategy{top:1337px;height:395px;background:var(--light)}
.creative{top:2098px;height:0}
.creative{top:1732px;height:366px;background:var(--light)}

/* services */
.services{top:2098px;height:433px;background:var(--sky)}
.services h2{position:absolute;left:100px;top:60px;font-size:44px;line-height:52px;color:var(--white)}
.explore{left:100px;top:331px;color:var(--white);font-size:15px}
.svc{position:absolute;width:200px;text-align:center}
.svc .ico{width:84px;height:84px;margin:0 auto;border-radius:50%;background:var(--white);display:flex;align-items:center;justify-content:center}
.svc span{display:block;margin-top:14px;color:var(--white);font-weight:700;font-size:17px}

/* faq */
.faq{top:2531px;height:441px;background:var(--white)}
.faq h2{position:absolute;left:0;width:1200px;top:65px;text-align:center;font-size:31px;color:var(--ink)}
.faq h2 i{display:block;width:40px;height:5px;background:var(--red);margin:4px auto 0}
.q{position:absolute;left:100px;width:990px;font-size:18px;color:var(--ink);text-transform:uppercase}
.q .tog{position:absolute;right:0;top:0;width:25px;height:25px;border-radius:50%;background:var(--sky);color:var(--white);font-size:22px;line-height:24px;text-align:center}
.answer{position:absolute;left:100px;top:192px;width:1000px;font-size:15px;line-height:20px;color:var(--text)}

/* testimonials */
.testimonials{top:2972px;height:307px;background:linear-gradient(90deg,#3d74b8,#4b86c9 50%,#3d74b8)}
.testimonials h2{position:absolute;left:0;width:1200px;top:65px;text-align:center;font-size:31px;color:var(--white)}
.quote{left:150px;top:150px;width:800px;color:var(--white);font-size:18px;line-height:25px}
.who{right:150px;top:200px;color:var(--white);font-weight:600;font-size:17px;text-transform:uppercase}
.arrow{top:168px;width:35px;height:35px;border:1px solid rgba(255,255,255,.7);background:rgba(255,255,255,.2);display:flex;align-items:center;justify-content:center}

/* contact */
.contact{top:3279px;height:309px;background:var(--dark)}
.contact h2{position:absolute;left:0;width:1200px;top:70px;text-align:center;font-size:31px;color:var(--white)}
.field{position:absolute;top:149px;width:251px}
.field label{display:block;color:#ddd;font-size:15px;margin-bottom:8px}
.field div{height:42px;background:var(--white)}
.submit{left:963px;top:168px;width:120px;height:42px;background:var(--red);border:1px solid #fff;color:var(--white);font-family:"Fjalla One",sans-serif;font-size:18px;display:flex;align-items:center;justify-content:center}
.copyright{left:0;width:1200px;top:263px;text-align:center;color:#ddd;font-size:13px}
.copyright b{color:var(--red);font-weight:400}
</style>
</head>
<body>

<section class="hero">
  <div class="abs stripes-top"></div>
  <div class="abs brand"><div class="brand-dot"></div><span class="brand-name">Copper Brook</span></div>
  <div class="abs phone">
    <svg width="28" height="28" viewBox="0 0 24 24" fill="none" stroke="#fff" stroke-width="1.6"><path d="M5 3l4 1 1 4-2 2a12 12 0 006 6l2-2 4 1 1 4-2 2C10 21 3 14 3 5z"/><path d="M14 3a7 7 0 017 7M14 6a4 4 0 014 4"/></svg>
    1-000-555-0142
  </div>
  <h1 class="abs head hero-title">Our clients pay<br>for our <span class="mark">Art</span><br>not our furniture</h1>
  <div class="abs stripes"></div>
  <div class="abs hero-art" role="img" aria-label="Illustration of tiny figures climbing red, white and black blocks among clouds"></div>
</section>

<section class="intro" role="img" aria-label="Background photo of a smiling man at a desk">
  <div class="abs down"><svg width="26" height="14" viewBox="0 0 26 14" fill="none" stroke="#33a6d7" stroke-width="2"><path d="M1 1l12 12L25 1"/></svg></div>
  <p>Copper Brook is a creative constellation. We are built on what’s great about the shared economy. With access to thousands of content creators, designers, technicians, writers, strategists and other creatives around the world, we are built differently than a traditional “brick and mortar” Marketing Agency. We provide the traditional services our clients have come to expect, without the “5X factor” of covering the overhead common in the old agency model. We believe even better work can be created in collaboration with our clients and by passing those savings back to them for their use. Our clients pay for our art, our work and our passion –not our furniture.</p>
</section>

<section class="row discovery">
  <div class="photo" style="left:0;background:linear-gradient(180deg,#dfe5e8 0%,#9fb0ba 45%,#4c6672 75%,#3b4a3a 100%)" role="img" aria-label="Photo of a hiker standing on a cliff above a mountain lake"></div>
  <div class="copy" style="left:640px;top:62px">
    <h2 class="head">Discovery</h2>
    <h3>We are passionate about creating with you, not just for you.</h3>
    <p>A facilitated Discovery conversation helps us to understand more about you, your mission, your aesthetic, your passion points and your narrative. In Discovery we look for your “why”, find what moves you and shape ideas together about content and strategies that will propel your mission forward.</p>
  </div>
</section>

<section class="row strategy">
  <div class="copy" style="left:100px;top:62px;width:470px">
    <h2 class="head">Strategy</h2>
    <h3>Content is only as good as your plan to deliver it.</h3>
    <p>Let’s face it, you can have the coolest car in the neighborhood but if its hidden in the garage or the gas tank is empty - no one is going to know about it. Strategies to deliver, maintain and build on what we are creating together is vital. Whether a single project or a years’ long collaboration Copper Brook shapes a strategy with you on how to deploy your creative.</p>
  </div>
  <div class="photo" style="left:600px;background:linear-gradient(135deg,#6f8a99 0%,#3d5566 50%,#1f2d36 100%)" role="img" aria-label="Photo of black and white chess pieces on a board"></div>
</section>

<section class="row creative">
  <div class="photo" style="left:0;background:radial-gradient(circle at 60% 40%,#ffd9a0 0%,#d4874a 25%,#3d5a78 70%,#2c4460 100%)" role="img" aria-label="Photo of a hand holding a glowing light bulb"></div>
  <div class="copy" style="left:640px;top:62px">
    <h2 class="head">Creative</h2>
    <h3>We are ready for our close up! Are you?</h3>
    <p>Copper Brook delivers imaginative, innovative, relatable content to clients looking to bring the “why” about their work into their messaging. Even a single image can reflect your core values, your passion points and your mission. Copper Brook scales our team of creatives in alignment with your goals, deploying a team of creatives who believe in the power of connectivity and community.</p>
  </div>
</section>

<section class="services">
  <h2 class="head">What<br>we do</h2>
  <div class="abs explore">Explore All Services &nbsp;›</div>
  <div class="svc" style="left:361px;top:63px"><div class="ico"><svg width="44" height="44" viewBox="0 0 24 24" fill="none" stroke="#33a6d7" stroke-width="2"><path d="M12 12l9 9M4 4l2 2M12 2v3M2 12h3M4 20l2-2M20 4l-2 2"/></svg></div><span>STRATEGY</span></div>
  <div class="svc" style="left:546px;top:63px"><div class="ico"><svg width="44" height="44" viewBox="0 0 24 24" fill="none" stroke="#33a6d7" stroke-width="2.4"><path d="M4 20L20 4M4 4l16 16"/></svg></div><span>CREATIVE</span></div>
  <div class="svc" style="left:730px;top:63px"><div class="ico"><svg width="44" height="44" viewBox="0 0 24 24" fill="none" stroke="#33a6d7" stroke-width="2"><path d="M3 3v18h18M6 16l4-5 4 3 5-7"/></svg></div><span>PAID MEDIA</span></div>
  <div class="svc" style="left:913px;top:63px"><div class="ico"><svg width="44" height="44" viewBox="0 0 24 24" fill="#33a6d7"><circle cx="8" cy="5" r="2"/><circle cx="14" cy="5" r="2"/><circle cx="8" cy="11" r="2"/><rect x="7" y="13" width="10" height="8" rx="3"/></svg></div><span>BROOKSMART</span></div>
  <div class="svc" style="left:361px;top:230px"><div class="ico"><svg width="44" height="44" viewBox="0 0 24 24" fill="none" stroke="#33a6d7" stroke-width="2"><path d="M2 4h3l3 11h11l2-8H6"/><circle cx="9" cy="19" r="1.6"/><circle cx="17" cy="19" r="1.6"/></svg></div><span>ECOMMERCE</span></div>
  <div class="svc" style="left:546px;top:230px"><div class="ico"><svg width="44" height="44" viewBox="0 0 24 24" fill="#3277b5"><circle cx="8" cy="7" r="3"/><circle cx="15" cy="7" r="3"/><rect x="4" y="11" width="13" height="9" rx="1"/><path d="M17 14l5-3v9l-5-3z"/></svg></div><span>PRODUCTION</span></div>
  <div class="svc" style="left:730px;top:230px"><div class="ico"><svg width="44" height="44" viewBox="0 0 24 24" fill="none" stroke="#33a6d7" stroke-width="2"><rect x="6" y="6" width="12" height="12"/><path d="M9 2v4M15 2v4M9 18v4M15 18v4M2 9h4M2 15h4M18 9h4M18 15h4"/></svg></div><span>4DS</span></div>
  <div class="svc" style="left:913px;top:230px"><div class="ico"><svg width="44" height="44" viewBox="0 0 24 24" fill="#33a6d7"><rect x="10" y="4" width="3" height="10" rx="1.5"/><rect x="7" y="11" width="11" height="10" rx="4"/></svg></div><span>BROOKEXPERIENCE</span></div>
</section>

<section class="faq">
  <h2 class="head">FAQ<i></i></h2>
  <div class="q" style="top:141px">What is a creative constellation?<span class="tog">−</span></div>
  <p class="answer">A Creative Constellation is a network of vendors, designers and creatives brought together by Copper Brook to support your campaign or project. After Discovery, your Copper Brook Creative Director chooses, from our roster of highly skilled Creatives, the most appropriate team members for your vision, aesthetic and goals. What’s better? A creative constellation is a living, animated creative team that can evolve as your needs</p>
  <div class="q" style="top:282px">How is a creative constellation managed?<span class="tog">+</span></div>
  <div class="q" style="top:341px">Is a creative constellation better than a traditional agency?<span class="tog">+</span></div>
</section>

<section class="testimonials" role="img" aria-label="Blue tinted background of client portrait photos">
  <h2 class="head">Testimonials</h2>
  <div class="abs arrow" style="left:100px"><svg width="12" height="20" viewBox="0 0 12 20" fill="none" stroke="#fff" stroke-width="1.6"><path d="M11 1L1 10l10 9"/></svg></div>
  <p class="abs quote">“Copper Brook is proving to be a force in the creative consulting industry and we look forward to collaborating with them again in the future.”</p>
  <div class="abs who">Dana Whitfield, Harbor Playhouse</div>
  <div class="abs arrow" style="left:1070px"><svg width="12" height="20" viewBox="0 0 12 20" fill="none" stroke="#fff" stroke-width="1.6"><path d="M1 1l10 9-10 9"/></svg></div>
</section>

<section class="contact">
  <h2 class="head">Contact us</h2>
  <div class="field" style="left:160px"><label>Name</label><div></div></div>
  <div class="field" style="left:427px"><label>Email</label><div></div></div>
  <div class="field" style="left:696px"><label>Phone</label><div></div></div>
  <div class="abs submit">SUBMIT</div>
  <div class="abs copyright">Copyright © 2019 <b>Copper Brook</b>. All rights reserved.</div>
</section>

</body>
</html>
```